Steadfast sons flyer

Benefits of prayer
- Prayer connects you to the God of fullness. Gal. 6:8
- Prayer places you cares on the Lord. 1 Peter 5:7, Matt. 11:28
- Prayer makes you fruitful in the vineyard of the Lord-this brings honour and glory. John 15:2
- Through prayer you exercise your Kingly authority. Matt. 16:19, 18:19.
- Prayer transforms you to be like Him. Luke 9:29.
- Prayer quickens divine inheritance. Luke 5:3-6
- Prayer will stir divine potentials in you. 2 Tim. 1:6
- And many more!

Experience the might and possibilities of prayer.

Join the Steadfast Sons Ministry!

```html
<!DOCTYPE html>
<html lang="en">
<head>
<meta charset="utf-8">
<title>Steadfast Sons Flyer – Benefits of Prayer</title>
<link href="https://fonts.googleapis.com/css2?family=Great+Vibes&family=PT+Sans:wght@400&family=Fira+Sans+Condensed:ital,wght@1,600&display=swap" rel="stylesheet">
<style>
  :root {
    --page-bg: #1c1c1c;
    --navy: #0a1a30;
    --navy-mid: #1f3550;
    --sky-light: #eef0f1;
    --sky-teal: #7fa3ab;
    --white: #ffffff;
    --brand-blue: #23466f;
    --brand-ring: #2a8a8c;
  }
  * { margin: 0; padding: 0; box-sizing: border-box; }
  html, body {
    width: 1200px; height: 1092px; overflow: hidden;
    background: var(--page-bg);
  }
  .flyer {
    position: absolute; left: 228px; top: 70px;
    width: 734px; height: 954px;
    background: var(--navy);
    overflow: hidden;
    color: var(--white);
    font-family: "PT Sans", sans-serif;
  }
  .flyer__photo {
    position: absolute; inset: 0 0 auto 0; height: 620px;
    background:
      radial-gradient(ellipse 60% 45% at 95% 22%, rgba(127,163,171,.75), transparent 70%),
      radial-gradient(ellipse 70% 55% at 30% 8%, rgba(255,255,255,.95), transparent 70%),
      linear-gradient(180deg, var(--sky-light) 0%, #b7c3c9 26%, #5d7387 48%, var(--navy-mid) 72%, var(--navy) 100%);
  }
  .brand {
    position: absolute; left: 44px; top: 72px;
    display: flex; align-items: center; gap: 14px;
  }
  .brand__dot {
    width: 64px; height: 64px; border-radius: 50%;
    background: var(--brand-ring);
  }
  .brand__name {
    font-family: "PT Sans", sans-serif;
    font-size: 20px; color: var(--brand-blue);
  }
  .title {
    position: absolute; left: 46px; top: 248px;
    font-family: "Great Vibes", cursive;
    font-weight: 400; font-size: 66px; line-height: 1;
    color: var(--white);
  }
  .benefits {
    position: absolute; left: 44px; top: 347px; width: 660px;
    list-style: none;
  }
  .benefits li {
    position: relative; padding-left: 25px;
    font-size: 19px; line-height: 26px;
    margin-bottom: 26px;
  }
  .benefits li::before {
    content: ""; position: absolute; left: 0; top: 6px;
    width: 14px; height: 14px; border-radius: 50%;
    background: var(--white);
  }
  .benefits li.benefits__more::before { display: none; }
  .cta {
    position: absolute; left: 40px;
    font-family: "Fira Sans Condensed", sans-serif;
    font-style: italic; font-weight: 600;
    letter-spacing: -0.5px;
  }
  .cta--lead { top: 794px; font-size: 27px; }
  .cta--join { top: 842px; font-size: 38px; }
</style>
</head>
<body>
  <main class="flyer">
    <div class="flyer__photo" role="img" aria-label="Photo of raised hands silhouetted against a bright sky with butterflies flying upward"></div>

    <div class="brand">
      <span class="brand__dot"></span>
      <span class="brand__name">Covenant Brothers Fellowship</span>
    </div>

    <h1 class="title">Benefits of prayer</h1>

    <ul class="benefits">
      <li>Prayer connects you to the God of fullness. Gal. 6:8</li>
      <li>Prayer places you cares on the Lord. 1 Peter 5:7, Matt. 11:28</li>
      <li>Prayer makes you fruitful in the vineyard of the Lord-this<br>brings honour and glory. John 15:2</li>
      <li>Through prayer you exercise your Kingly authority. Matt. 16:19, 18:19.</li>
      <li>Prayer transforms you to be like Him. Luke 9:29.</li>
      <li>Prayer quickens divine inheritance. Luke 5:3-6</li>
      <li>Prayer will stir divine potentials in you. 2 Tim. 1:6</li>
      <li class="benefits__more">And many more!</li>
    </ul>

    <p class="cta cta--lead">Experience the might and possibilities of prayer.</p>
    <p class="cta cta--join">Join the Steadfast Sons Ministry!</p>
  </main>
</body>
</html>
```